Stationery Design Project

Our company is "Meridian Softworks" and we have a product called "ledgerpine.com". The product is an online accounting software for businesses. We want to communicate that our software will help business owners to be more efficient and help them track their finances better. Ledgerpine.com is basically a simple version of tallyworks.

"We want a unique and creative design which will surprise our customer."

NAME CARD = LEDGERPINE
We want a ledgerpine name card NOT MERIDIAN SOFTWORKS.

For the content of the name card, please make sure it fit with a long name like the following:

Rudi Hartono Alias Rudi
Developer Specialist
T: (021) 5172 4480
F: (021) 5172 4481
E: customer.service@mrd-soft.example

I need you to put it the following information to the name card

"ledgerpine"
- moto is "automate your businesses"
- website "www.ledgerpine.com"
- ledgerpine is a "Web Accounting Software"
- product of "Meridian Softworks"

LETTERHEAD, ENVELOPE, FOLDER = MERIDIAN SOFTWORKS
Other than name card we wanted you to design for us; letterhead, envelope and folder. In letterhead, envelope and folder it should ONLY contain the following information ("Meridian Softworks").
PLEASE BE SURE YOU ARE NOT PUTTING "LEDGERPINE LOGO" IN LETTERHEAD, ENVELOPE AND FOLDER.

"Meridian Softworks"
Address:
Ruko Kirana Plaza Blok. D No. 17
Jl. Wijayakusuma No. 48
Jakarta
Kebayoran, 12450
Indonesia

Web Address: mrd-soft.example

T: (021) 5172 4480
F: (021) 5172 4481

Target Market(s)

Business Owners, Accountant, Auditor, Tax Consultant

Industry/Entity Type

Accounting

```html
<!DOCTYPE html>
<html lang="en">
<head>
<meta charset="utf-8">
<title>Meridian Softworks — Envelope</title>
<link rel="stylesheet" href="https://fonts.googleapis.com/css2?family=Questrial&family=Open+Sans:wght@400;600&display=swap">
<style>
  :root {
    --backdrop: #e4e4e2;
    --paper: #ffffff;
    --ink: #3c3e40;
    --brand-grey: #6b6e72;
    --brand-green: #5a9e1f;
    --mark-grey: #9a9da1;
  }
  * { margin: 0; padding: 0; box-sizing: border-box; }
  html, body {
    width: 1200px; height: 720px; overflow: hidden;
    background: var(--backdrop);
  }
  .canvas {
    position: relative; width: 1200px; height: 720px;
  }
  .envelope {
    position: absolute; left: 80px; top: 100px;
    width: 1040px; height: 520px;
    background: var(--paper);
    box-shadow: 0 2px 10px rgba(0,0,0,0.12);
  }
  .brand {
    position: absolute; left: 44px; top: 40px;
    display: flex; align-items: center; gap: 14px;
  }
  .brand-dot {
    width: 62px; height: 62px; border-radius: 50%;
    background: var(--mark-grey);
  }
  .brand-name {
    font-family: "Questrial", sans-serif;
    font-size: 34px; letter-spacing: 2px;
    color: var(--brand-grey);
  }
  .contact {
    position: absolute; left: 44px; top: 124px;
    font-family: "Open Sans", sans-serif;
    font-size: 12px; line-height: 17px; color: var(--ink);
    list-style: none;
  }
  .contact li { display: flex; align-items: center; gap: 7px; }
  .contact svg { width: 11px; height: 11px; flex: none; }
  .address {
    position: absolute; left: 294px; top: 132px;
    font-family: "Open Sans", sans-serif; font-style: normal;
    font-size: 12px; line-height: 17px; color: var(--ink);
  }
  .web {
    position: absolute; left: 0; top: 432px;
    display: flex; align-items: center; gap: 8px;
  }
  .web-bar {
    width: 84px; height: 8px; background: var(--brand-green);
  }
  .web-url {
    font-family: "Open Sans", sans-serif;
    font-size: 20px; color: var(--brand-green);
  }
</style>
</head>
<body>
<main class="canvas">
  <section class="envelope">
    <div class="brand">
      <span class="brand-dot"></span>
      <span class="brand-name">MERIDIAN SOFTWORKS</span>
    </div>

    <ul class="contact">
      <li>
        <svg viewBox="0 0 12 12" aria-hidden="true"><rect width="12" height="12" rx="1.5" fill="var(--brand-green)"/><path d="M3.5 2.5h1.5l.7 2-1 .8a5 5 0 0 0 2 2l.8-1 2 .7v1.5c0 .5-.4.9-.9.9A6.6 6.6 0 0 1 2.6 3.4c0-.5.4-.9.9-.9z" fill="#fff"/></svg>
        (021) 5172 4480
      </li>
      <li>
        <svg viewBox="0 0 12 12" aria-hidden="true"><rect width="12" height="12" rx="1.5" fill="var(--brand-green)"/><rect x="3.5" y="2" width="5" height="3" fill="#fff"/><rect x="2" y="5.5" width="8" height="4" rx="0.8" fill="#fff"/></svg>
        (021) 5172 4481
      </li>
      <li>
        <svg viewBox="0 0 12 12" aria-hidden="true"><rect width="12" height="12" rx="1.5" fill="var(--brand-green)"/><rect x="2" y="3.3" width="8" height="5.4" fill="#fff"/><path d="M2 3.3l4 3 4-3" fill="none" stroke="var(--brand-green)" stroke-width="0.9"/></svg>
        customer.service@mrd-soft.example
      </li>
    </ul>

    <address class="address">
      Ruko Kirana Plaza Blok. D No. 17<br>
      Jl. Wijayakusuma No. 48<br>
      Jakarta, Kebayoran, 12450, Indonesia
    </address>

    <div class="web">
      <span class="web-bar"></span>
      <span class="web-url">mrd-soft.example</span>
    </div>
  </section>
</main>
</body>
</html>
```